Pelunor Mobile phone

Please can you design a box for a mobile phone.
Dimensions so that the phone
and a USB cable can fit into it.

Additional phones have been added model names have been changed to KMV

KMV350 Mobile phone dimensions
1.2 cm thick

11.3 cm x 6.2 cm

KMV400
128mm*64.5mm*9.5mm

KMV500
146mm*72mm*10.5mm

KMV550 Mobile phone dimensions

.09 cm thick
157mm*78mm*9.5mm

Please put the name Pelunor (Gill San font)
I have also supplied the company logo this will not need to be changed.
I have added images of the phones that the packaging is being designed for. . along with this I have added an example of the instructions that will be inside the packaging. 16.04.14

*The packaging must be scalable so that there is packaging for each of the 4 models* 06.06.2014

Target Market(s)

Quivenel Mobile phone Market

Industry/Entity Type

It Company

Font styles to use
Sans Serif
Other font styles liked:
• Gill Sans

Requirements
Must have
• The design must be on a box that will be foldable so it is laid out in one flat sheet.
the font for the word Pelunor must be Gill Sans.

A design for each phone ( different sizes for each phone).

This has been added 09/05/2014 please can you also provide step by step instructions on how to fold the boxes.

```html
<!DOCTYPE html>
<html lang="en">
<head>
<meta charset="utf-8">
<title>Pelunor KMV500 – Box Dieline</title>
<link rel="stylesheet" href="https://fonts.googleapis.com/css2?family=Cabin:wght@400;500&display=swap">
<style>
  :root {
    --paper: #ffffff;
    --frame: #2b2b2b;
    --cut-line: #333333;
    --ink: #2a2a2a;
    --brand-dot: #f2cf1f;
    --device-body: #1d1f1f;
  }
  html, body {
    margin: 0;
    padding: 0;
    width: 1200px;
    height: 1000px;
    overflow: hidden;
    background: var(--paper);
  }
  .sheet {
    position: relative;
    width: 1200px;
    height: 1000px;
  }
  .sheet__frame {
    position: absolute;
    left: 19px;
    top: 16px;
    width: 1152px;
    height: 954px;
    border: 6px solid var(--frame);
  }
  .dieline {
    position: absolute;
    inset: 0;
  }
  .cut {
    fill: none;
    stroke: var(--cut-line);
    stroke-width: 1;
  }
  .brand-name {
    font-family: "Cabin", sans-serif;
    font-weight: 400;
    fill: var(--ink);
    letter-spacing: 0.5px;
  }
  .model-code {
    font-family: "Cabin", sans-serif;
    font-weight: 400;
    fill: var(--ink);
  }
  .spec-label {
    font-family: "Cabin", sans-serif;
    font-size: 7.5px;
    fill: var(--ink);
  }
  .spec-icon { fill: var(--ink); }
  .spec-rule { stroke: var(--ink); stroke-width: 0.8; }
  .brand-dot { fill: var(--brand-dot); }
  .device-illustration { fill: var(--device-body); }
</style>
</head>
<body>
<div class="sheet">
  <div class="sheet__frame"></div>

  <svg class="dieline" width="1200" height="1000" viewBox="0 0 1200 1000" xmlns="http://www.w3.org/2000/svg">

    <!-- Inner tray insert -->
    <g class="insert">
      <rect class="cut" x="77" y="313" width="357" height="381"/>
      <line class="cut" x1="162" y1="313" x2="162" y2="694"/>
      <line class="cut" x1="181" y1="313" x2="181" y2="694"/>
      <line class="cut" x1="415" y1="313" x2="415" y2="694"/>
      <polyline class="cut" points="209,313 209,435 194,435 194,573 209,573 209,694"/>
      <polyline class="cut" points="386,313 386,435 402,435 402,573 386,573 386,694"/>
      <circle class="cut" cx="298" cy="504" r="32"/>
      <rect class="cut" x="271" y="329" width="54" height="4"/>
      <rect class="cut" x="271" y="674" width="54" height="4"/>
      <!-- top locking flap -->
      <polyline class="cut" points="212,313 212,240 273,240 273,228 323,228 323,240 384,240 384,313"/>
      <line class="cut" x1="212" y1="266" x2="384" y2="266"/>
      <line class="cut" x1="212" y1="285" x2="384" y2="285"/>
      <!-- bottom locking flap -->
      <polyline class="cut" points="212,694 212,768 273,768 273,780 323,780 323,768 384,768 384,694"/>
      <line class="cut" x1="212" y1="723" x2="384" y2="723"/>
      <line class="cut" x1="212" y1="742" x2="384" y2="742"/>
    </g>

    <!-- Glue side panel -->
    <g class="panel panel--side-left">
      <rect class="cut" x="434" y="311" width="88" height="385"/>
      <rect class="cut" x="436" y="223" width="83" height="88"/>
      <rect class="cut" x="436" y="696" width="83" height="88"/>
    </g>

    <!-- Back panel with specifications -->
    <g class="panel panel--back">
      <rect class="cut" x="522" y="311" width="214" height="385"/>
      <rect class="cut" x="522" y="223" width="213" height="88"/>
      <rect class="cut" x="525" y="137" width="208" height="86"/>
      <rect class="cut" x="522" y="696" width="213" height="88"/>
      <rect class="cut" x="525" y="784" width="208" height="86"/>

      <text class="brand-name" x="720" y="344" font-size="17" text-anchor="end">PELUNOR</text>
      <text class="model-code" x="720" y="352" font-size="9" text-anchor="end">KMV500</text>

      <g class="spec-list">
        <!-- screen size -->
        <rect x="580" y="385" width="11" height="17" rx="1.5" fill="none" stroke="#2a2a2a" stroke-width="1.4"/>
        <text class="spec-label" x="650" y="397" text-anchor="middle">Screen Size</text>
        <line class="spec-rule" x1="556" y1="406" x2="700" y2="406"/>
        <!-- operating software -->
        <rect class="spec-icon" x="579" y="412" width="13" height="14" rx="2"/>
        <text class="spec-label" x="650" y="422" text-anchor="middle">Quivenel Software</text>
        <line class="spec-rule" x1="556" y1="432" x2="700" y2="432"/>
        <!-- camera -->
        <rect class="spec-icon" x="577" y="439" width="16" height="11" rx="1"/>
        <circle cx="585" cy="444.5" r="2.6" fill="#fff"/>
        <text class="spec-label" x="650" y="447" text-anchor="middle">MegaPixels</text>
        <line class="spec-rule" x1="556" y1="457" x2="700" y2="457"/>
        <!-- memory card -->
        <rect class="spec-icon" x="580" y="463" width="12" height="15"/>
        <text class="spec-label" x="650" y="472" text-anchor="middle">Internal Memory</text>
        <line class="spec-rule" x1="556" y1="483" x2="700" y2="483"/>
        <!-- RAM -->
        <path class="spec-icon" d="M577 490 h10 l3 3 h5 v8 h-18 z"/>
        <text class="spec-label" x="650" y="499" text-anchor="middle">RAM</text>
        <line class="spec-rule" x1="556" y1="508" x2="700" y2="508"/>
        <!-- processor -->
        <rect class="spec-icon" x="578" y="514" width="15" height="14"/>
        <rect x="582" y="518" width="7" height="6" fill="#fff"/>
        <text class="spec-label" x="650" y="524" text-anchor="middle">Processor</text>
        <line class="spec-rule" x1="556" y1="534" x2="700" y2="534"/>
        <!-- battery -->
        <rect class="spec-icon" x="576" y="541" width="19" height="9"/>
        <rect class="spec-icon" x="575" y="543" width="2" height="5"/>
        <text class="spec-label" x="650" y="549" text-anchor="middle">Battery</text>
      </g>
    </g>

    <!-- Side panel -->
    <g class="panel panel--side">
      <rect class="cut" x="736" y="311" width="88" height="385"/>
      <rect class="cut" x="738" y="223" width="83" height="88"/>
      <rect class="cut" x="738" y="696" width="83" height="88"/>
      <text class="brand-name" x="0" y="0" font-size="26" letter-spacing="1.5" text-anchor="middle" transform="translate(771 504) rotate(90)">PELUNOR</text>
    </g>

    <!-- Front panel -->
    <g class="panel panel--front">
      <rect class="cut" x="824" y="311" width="213" height="385"/>
      <circle class="brand-dot" cx="886" cy="338" r="17"/>
      <text class="brand-name" x="909" y="342" font-size="15">PELUNOR</text>
      <text class="model-code" x="985" y="350" font-size="9" text-anchor="end">KMV500</text>
      <rect class="device-illustration" x="847" y="367" width="167" height="330" rx="12"
            role="img" aria-label="Front view of the KMV500 smartphone with its screen"/>
    </g>

    <!-- Closing side panel -->
    <g class="panel panel--side-right">
      <rect class="cut" x="1037" y="313" width="88" height="381"/>
      <path class="cut" d="M1042 313 V233 H1072 C1112 233 1120 240 1120 280 V313"/>
      <path class="cut" d="M1042 694 V775 H1072 C1112 775 1120 768 1120 728 V694"/>
      <text class="brand-name" x="0" y="0" font-size="26" letter-spacing="1.5" text-anchor="middle" transform="translate(1090 504) rotate(-90)">PELUNOR</text>
    </g>
  </svg>
</div>
</body>
</html>
```